Corvid Aviation - Learn to Fly

Our customers are people who span all ages and genders that are interested in learning how to fly airplanes for fun or as a career, or who would like to advance their piloting skills.

Flight training we offer:
Private Pilot Certificate
Instrument Rating
Commercial Pilot Certificate
Sport Pilot Certificate: Powered Parachute
Drone Pilot Training

Ground School we offer:
Sport Pilot Ground School
Private Pilot Ground School
Instrument Pilot Ground School
Drone Pilot Ground School

Target Market(s)

Bessemer, Alabama, United States: High school students, college students, career changers. Someone interested in learning to fly for fun or for a career in the United States.

Industry/Entity Type

Aviation

Requirements
Must have
• I would like for you to enjoy some creative freedom here. The feeling and image we want to portray is a professional, but also very exciting and energizing image. The prospective customer and student should see the brochure and be excited to call us or come out for more information on learning how to fly. Our tag line is: "Small Step Today, Giant Leap Tomorrow."
Nice to have
• It would be helpful if you can do some reading or a little research on each of the types of training that we offer so that you will understand what should be included in the brochure. Our goal is to let everyone know who we are, what we offer, and how to contact us.

This may help some with design ideas: The name Corvid Aviation is inspired by the Orbix Skyward space program because the owner of the flight school is a big fan of Orbix and the Skyward mission.

```html
<!DOCTYPE html>
<html lang="en">
<head>
<meta charset="UTF-8">
<title>Corvid Aviation – What We Offer</title>
<link rel="stylesheet" href="https://fonts.googleapis.com/css2?family=Poppins:ital,wght@0,400;0,600;0,700;1,300&display=swap">
<style>
  :root {
    --gold: #f7c531;
    --white: #ffffff;
    --rule: #f3e6d2;
    --sky-top: #5a4a78;
    --sky-mid: #a06f8e;
    --sky-glow: #d79a8e;
    --sky-low: #7d6884;
    --ground: #5c566a;
    --tint: rgba(70, 40, 95, 0.35);
  }
  * { box-sizing: border-box; margin: 0; padding: 0; }
  html, body {
    width: 1200px; height: 857px; overflow: hidden;
    background: #2a2035;
  }
  .panel {
    position: relative;
    width: 1200px; height: 857px;
    overflow: hidden;
    font-family: "Poppins", sans-serif;
    color: var(--white);
  }
  .hero-photo {
    position: absolute; inset: 0;
    background:
      radial-gradient(ellipse 70% 45% at 55% 40%, var(--sky-glow) 0%, rgba(215,154,142,0) 70%),
      linear-gradient(180deg, var(--sky-top) 0%, var(--sky-mid) 38%, var(--sky-low) 70%, var(--ground) 100%);
  }
  .hero-photo::after {
    content: ""; position: absolute; inset: 0;
    background: var(--tint);
  }
  .headline {
    position: absolute; left: 76px; top: 88px;
    font-weight: 700; font-size: 88px; line-height: 92px;
    letter-spacing: 6px; color: var(--gold);
  }
  .headline-rule {
    position: absolute; left: 393px; top: 348px;
    width: 655px; height: 3px; background: var(--rule);
  }
  .offer-list {
    position: absolute; top: 418px;
    list-style: none;
  }
  .offer-list h2 {
    font-weight: 700; font-size: 30px; line-height: 44px;
    margin-bottom: 4px;
  }
  .offer-list li {
    font-weight: 400; font-size: 31px; line-height: 40px;
  }
  .offer-list .indent { padding-left: 30px; }
  .flight-training { left: 76px; }
  .ground-school { right: 46px; text-align: right; }
  .tagline {
    position: absolute; left: 0; right: 0; top: 800px;
    text-align: center;
    font-style: italic; font-weight: 300; font-size: 29px;
    color: var(--gold);
  }
</style>
</head>
<body>
<main class="panel">
  <div class="hero-photo" role="img" aria-label="Red aerobatic plane flying between race pylons against a purple sunset sky with a smoke trail"></div>

  <h1 class="headline">WHAT<br>WE<br>OFFER</h1>
  <div class="headline-rule"></div>

  <section class="offer-list flight-training">
    <h2>Flight training :</h2>
    <ul style="list-style:none">
      <li>• Private Pilot Certificate</li>
      <li>• Instrument Rating</li>
      <li>• Commercial Pilot Certificate</li>
      <li>• Sport Pilot Certificate:</li>
      <li class="indent">Powered Parachute</li>
      <li>• Drone Pilot Training</li>
    </ul>
  </section>

  <section class="offer-list ground-school">
    <h2>Ground School training :</h2>
    <ul style="list-style:none">
      <li>• Sport Pilot Ground School</li>
      <li>• Private Pilot Ground School</li>
      <li>• Instrument Pilot Ground School</li>
      <li>• Drone Pilot Ground School</li>
    </ul>
  </section>

  <p class="tagline">Small Step Today,&nbsp; Giant Leap Tomorrow</p>
</main>
</body>
</html>
```